Welcome Card

We are a property management company and I need to attach this postcard to 2 packages of microwave popcorn as a welcome gift to our new tenant.Here is the copy for the postcard (FRONT SIDE): Just "popped" in to make sure your apartment was ready for you! Enjoy your Stay.........UNITED APARTMENTSBACK SIDE: Welcome image with the words "Thank You"

It Company

Sans Serif

```html
<!DOCTYPE html>
<html lang="en">
<head>
<meta charset="utf-8">
<title>Meridale Apartments – Welcome Card</title>
<link rel="stylesheet" href="https://fonts.googleapis.com/css2?family=Caprasimo&family=Questrial&display=swap">
<style>
  :root {
    --backdrop: #e6e7ea;
    --brand-blue: #1d56a6;
    --brand-blue-light: #2a66b5;
    --card-white: #ffffff;
    --ink: #1a1a1a;
    --dash: #444444;
    --popcorn: #f3ecc4;
    --popcorn-shade: #e2d79a;
  }
  * { margin: 0; padding: 0; box-sizing: border-box; }
  html, body {
    width: 1200px; height: 1200px; overflow: hidden;
    background: var(--backdrop);
  }
  .canvas { position: relative; width: 1200px; height: 1200px; }

  /* Back side */
  .card-back {
    position: absolute; left: 448px; top: 36px;
    width: 718px; height: 552px;
    background: linear-gradient(180deg, var(--brand-blue-light) 0%, var(--brand-blue) 100%);
    display: flex; flex-direction: column; align-items: center; justify-content: center;
    color: #fff;
  }
  .card-back__title {
    font-family: "Caprasimo", serif;
    font-size: 66px; font-weight: 400; line-height: 1;
    margin-top: -30px;
  }
  .card-back__thanks {
    font-family: "Questrial", sans-serif;
    font-size: 27px; margin-top: 52px;
  }

  /* Front side */
  .card-front {
    position: absolute; left: 53px; top: 612px;
    width: 720px; height: 552px;
    background: var(--card-white);
    padding: 22px;
  }
  .card-front__frame {
    width: 100%; height: 100%;
    border: 3px solid var(--brand-blue);
    border-radius: 34px;
    padding: 7px;
  }
  .card-front__inner {
    width: 100%; height: 100%;
    border: 1.5px dashed var(--dash);
    border-radius: 26px;
    display: flex; flex-direction: column; align-items: center;
    padding-top: 30px;
  }
  .headline-small {
    font-family: "Caprasimo", serif;
    font-size: 36px; color: var(--ink); line-height: 1; letter-spacing: 1px;
  }
  .headline-popped {
    font-family: "Caprasimo", serif;
    font-size: 104px; color: var(--brand-blue); line-height: 1;
    display: flex; align-items: center; margin-top: 2px;
  }
  .popcorn-kernel {
    display: inline-block; width: 90px; height: 100px;
    margin: 0 2px 0 -4px;
    border-radius: 46% 50% 42% 48%;
    background: radial-gradient(circle at 45% 40%, var(--popcorn) 55%, var(--popcorn-shade) 100%);
    transform: translateY(6px);
  }
  .message {
    font-family: "Questrial", sans-serif;
    font-size: 21px; color: var(--ink); text-align: center; line-height: 1.35;
    margin-top: 22px;
  }
  .signoff {
    font-family: "Caprasimo", serif;
    font-size: 29px; color: var(--ink); letter-spacing: 1px;
    margin-top: 26px;
  }
  .brand-name {
    display: flex; align-items: center; gap: 12px;
    margin-top: 44px;
    font-family: "Questrial", sans-serif;
    font-size: 28px; color: var(--brand-blue); letter-spacing: 1px;
  }
  .brand-name__mark {
    width: 22px; height: 22px; background: var(--brand-blue);
  }
</style>
</head>
<body>
<main class="canvas">
  <section class="card-back" aria-label="Card back">
    <h1 class="card-back__title">Welcome</h1>
    <p class="card-back__thanks">Thank You</p>
  </section>

  <section class="card-front" aria-label="Card front">
    <div class="card-front__frame">
      <div class="card-front__inner">
        <p class="headline-small">JUST</p>
        <p class="headline-popped">p<span class="popcorn-kernel" role="img" aria-label="Popped popcorn kernel standing in for the letter o"></span>pped</p>
        <p class="message">in to make sure<br>your apartment was ready for you!</p>
        <p class="signoff">ENJOY YOUR STAY .......</p>
        <p class="brand-name"><span class="brand-name__mark"></span>MERIDALE APARTMENTS</p>
      </div>
    </div>
  </section>
</main>
</body>
</html>
```